Etiketten für Charity Bier gesucht
Zielgruppe
Wir engagieren uns ehrenamtlich für Kinder in Afrika.
In Einsatz-Teams von freiwilligen Helfern, sammeln wir während 8 Monaten Spendengelder, um Kindern in Townships's Südafrikas eine Zukunft zu bauen, in dem wir nicht staatliche Kindertagesstätten engagierter einheimischer Frauen umbauen.
Vorher bestehen die KITA's nur aus rostigen Wellblechhütten, welche nicht isoliert sind und auf dem KITA Gelände befindet sich weder Rasen, noch ein Spielplatz.
Aufgabenstellung
Um Spenden zu sammeln, möchten wir ein Charity Bier auf den Markt bringen.
Infos zu den Maßen der Etiketten: Sie sollten nicht breiter als 8 cm sein. Wichtig ist, dass sich in der Ecke links oben keine Angaben befinden, da die obere linke Kante schräg nach oben verlaufen wird. Welche Angaben müssen zwingend auf den Etiketten zu finden sein?
Die Promill-Angaben (5.2% VOL)
Inhalts-Angabe (33cl) das Logo des Bierherstellers sollte auch mit auf die Etikette (nicht all zu gross) (siehe Bild Nr.2)
Die Info's zum Bier (Biersorte: Hochmoosbräu KLASSIK)
Der Name des Bier's sollte Charity Bier sein.
Wir möchten auf der Etikette auch folgendes unbedingt vermerken:
'Diese Flache (Bier) füllt 10 Breischalen für Kinder in Afrika'
Ansonsten haben wir überhaupt keine Vorstellung, was wir wörtlich noch auf die Etikette packen möchten (vielleicht fällt euch ja noch was tolles ein:-)
Was wir uns vom Design her so vorstellen:
Ich habe noch 3 Bilder (siehe Bild 3-4) dazugefügt, mit Designs, welche mir auf Anhieb sehr sehr gut gefallen (damit ihr einen Anhaltspunkt habt:-) Aber ich lasse mich auch gerne von anderen Design-Formen überraschen.

```html
<!DOCTYPE html>
<html lang="de">
<head>
<meta charset="utf-8">
<title>Charity Bier – Etikett</title>
<link rel="stylesheet" href="https://fonts.googleapis.com/css2?family=Roboto+Slab:wght@400;700;800;900&family=Oswald:wght@400;500;600&display=swap">
<style>
  :root {
    --ink: #2b2a2c;
    --charity-red: #c8242b;
    --paper: #ffffff;
    --stage: #ecebe8;
    --muted: #5a595b;
    --map-light: #6a696b;
  }
  * { box-sizing: border-box; margin: 0; padding: 0; }
  html, body { width: 1200px; height: 2400px; overflow: hidden; }
  body {
    background: var(--stage);
    position: relative;
    font-family: "Oswald", sans-serif;
    color: var(--ink);
  }
  .label {
    position: absolute;
    left: 100px;
    top: 700px;
    width: 1000px;
    height: 1000px;
  }
  .label-frame { position: absolute; inset: 0; }
  .brewery-name {
    position: absolute;
    top: 125px; left: 0; width: 100%;
    text-align: center;
    font-family: "Roboto Slab", serif;
    font-weight: 700;
    font-size: 34px;
    color: var(--ink);
  }
  .info-row {
    position: absolute;
    top: 190px; left: 70px; right: 70px;
    height: 100px;
    display: flex;
    align-items: center;
    justify-content: space-between;
  }
  .info-note {
    width: 300px;
    text-align: center;
    font-size: 20px;
    letter-spacing: 3px;
    color: var(--muted);
    border-top: 2px solid var(--ink);
    border-bottom: 2px solid var(--ink);
    padding: 6px 0;
  }
  .africa-map {
    width: 100px; height: 100px;
    background: linear-gradient(160deg, var(--map-light), var(--ink));
  }
  .donation-band {
    position: absolute;
    top: 310px; left: 70px; right: 70px;
    background: var(--charity-red);
    color: var(--paper);
    text-align: center;
    font-family: "Roboto Slab", serif;
    font-weight: 700;
    font-size: 27px;
    line-height: 1.3;
    padding: 14px 20px;
    letter-spacing: 1px;
  }
  .beer-title {
    position: absolute;
    top: 445px; left: 0; width: 100%;
    text-align: center;
    font-family: "Roboto Slab", serif;
    font-weight: 900;
    font-size: 160px;
    line-height: 165px;
    letter-spacing: 1px;
  }
  .beer-title .word-charity { display: block; color: var(--ink); }
  .beer-title .word-bier { display: block; color: var(--charity-red); }
  .tagline {
    position: absolute;
    top: 805px; left: 0; width: 100%;
    text-align: center;
    font-family: "Roboto Slab", serif;
    font-weight: 700;
    font-size: 24px;
    letter-spacing: 1px;
    color: var(--ink);
  }
  .volume-pill {
    position: absolute;
    top: 855px; left: 50%;
    transform: translateX(-50%);
    border: 2px solid var(--ink);
    border-radius: 30px;
    padding: 4px 30px;
    font-size: 22px;
    letter-spacing: 2px;
    white-space: nowrap;
  }
  .month-notches {
    position: absolute;
    top: 922px; left: 60px; right: 60px;
    display: flex;
    justify-content: space-between;
    font-size: 17px;
    color: var(--muted);
  }
  .month-notches span {
    width: 60px;
    text-align: center;
    border-left: 2px solid var(--ink);
    padding-top: 4px;
  }
  .month-notches span:first-child { border-left: none; }
</style>
</head>
<body>
  <section class="label">
    <svg class="label-frame" width="1000" height="1000" viewBox="0 0 1000 1000" aria-hidden="true">
      <polygon points="0,90 1000,0 1000,1000 0,1000" fill="var(--ink)"/>
      <polygon points="24,111 976,26 976,976 24,976" fill="var(--paper)"/>
    </svg>

    <div class="brewery-name">Hochmoosbräu</div>

    <div class="info-row">
      <div class="info-note">FRISCH GEBRAUT</div>
      <div class="africa-map" role="img" aria-label="Karte des afrikanischen Kontinents"></div>
      <div class="info-note">AUS DER REGION</div>
    </div>

    <div class="donation-band">DIESE FLASCHE BIER FÜLLT 10 BREISCHALEN<br>FÜR KINDER IN AFRIKA</div>

    <h1 class="beer-title">
      <span class="word-charity">CHARITY</span>
      <span class="word-bier">BIER</span>
    </h1>

    <p class="tagline">(JEDER SCHLUCK HILFT EINEM KIND IN AFRIKA)</p>

    <div class="volume-pill">KLASSIK · 5.2% VOL · 33CL</div>

    <div class="month-notches">
      <span>1</span><span>2</span><span>3</span><span>4</span><span>5</span><span>6</span>
      <span>7</span><span>8</span><span>9</span><span>10</span><span>11</span><span>12</span>
    </div>
  </section>
</body>
</html>
```